RWP Tax Services
RWP Tax Services -
Creative Brief
Professional
Dan Feltwicke
President
2847 Harbor Street, Suite 210 San Jose, CA 95128
dan@rwptaxdemo.com
www.rwptaxdemo.com
We want the card to look and feel like it is a combination of real estate business card and CPA business card. Tax professional (CPA office) with photo (real estate business) of president.

```html
<!DOCTYPE html>
<html lang="en">
<head>
<meta charset="utf-8">
<title>RWP Tax Services – Business Card</title>
<link href="https://fonts.googleapis.com/css2?family=Arimo:wght@400;700&display=swap" rel="stylesheet">
<style>
  :root {
    --page-bg: #ffffff;
    --red-light: #d42420;
    --red-mid: #a8171a;
    --red-dark: #6e0d10;
    --band-dark: #2b201d;
    --gold: #c9a14c;
    --white: #ffffff;
    --logo-fill: #cd8552;
    --logo-text: #3a2416;
  }
  * { margin: 0; padding: 0; box-sizing: border-box; }
  html, body {
    width: 1200px;
    height: 917px;
    overflow: hidden;
    background: var(--page-bg);
    font-family: "Arimo", Arial, sans-serif;
  }
  .business-card {
    position: absolute;
    left: 237px;
    top: 234px;
    width: 726px;
    height: 449px;
    border-radius: 28px;
    overflow: hidden;
  }
  .card-art {
    position: absolute;
    inset: 0;
    width: 100%;
    height: 100%;
  }
  .logo-block {
    position: absolute;
    left: 464px;
    top: 52px;
    width: 166px;
    height: 149px;
    background: var(--logo-fill);
    border-radius: 12px;
    display: flex;
    align-items: center;
    justify-content: center;
    text-align: center;
    color: var(--logo-text);
    font-weight: 700;
    font-size: 25px;
    line-height: 1.15;
    padding: 0 14px;
  }
  .holder-name {
    position: absolute;
    left: 52px;
    top: 201px;
    color: var(--white);
    font-size: 44px;
    font-weight: 400;
    white-space: nowrap;
  }
  .holder-title {
    position: absolute;
    left: 140px;
    top: 249px;
    color: var(--white);
    font-size: 26px;
    white-space: nowrap;
  }
  .address {
    position: absolute;
    left: 32px;
    top: 358px;
    color: var(--gold);
    font-size: 21px;
    line-height: 25px;
    white-space: nowrap;
  }
  .contact-list {
    position: absolute;
    left: 399px;
    top: 292px;
    color: var(--gold);
    font-size: 21px;
    line-height: 25.5px;
    list-style: none;
    white-space: nowrap;
  }
  .contact-list .label {
    display: inline-block;
    width: 109px;
  }
  .contact-list .label-short {
    width: auto;
    margin-right: 10px;
  }
</style>
</head>
<body>
  <div class="business-card">
    <svg class="card-art" viewBox="0 0 726 449" preserveAspectRatio="none" aria-hidden="true">
      <defs>
        <radialGradient id="redGlow" cx="0.5" cy="0.55" r="0.75">
          <stop offset="0" stop-color="var(--red-light)"/>
          <stop offset="0.55" stop-color="var(--red-mid)"/>
          <stop offset="1" stop-color="var(--red-dark)"/>
        </radialGradient>
      </defs>
      <rect class="card-face" x="0" y="0" width="726" height="449" fill="url(#redGlow)"/>
      <path class="lower-band" d="M0,330 C150,346 270,318 400,265 C520,220 640,238 726,292 L726,449 L0,449 Z" fill="var(--band-dark)"/>
    </svg>

    <div class="logo-block">RWP Tax Services</div>

    <div class="holder-name">Dan Feltwicke</div>
    <div class="holder-title">President</div>

    <div class="address">
      2847 Harbor Street, Suite 210<br>
      San Jose, CA 95128
    </div>

    <ul class="contact-list">
      <li><span class="label">Toll free</span>(877) 555-0142</li>
      <li><span class="label">Phone</span>(408) 555-0163</li>
      <li><span class="label">Fax</span>(408) 555-0188</li>
      <li><span class="label label-short">Email</span>dan@rwptaxdemo.com</li>
      <li>www.rwptaxdemo.com</li>
    </ul>
  </div>
</body>
</html>
```